Elegant Black Candle Label Design!

I need a 2.375" tall by 3.0" wide candle label design. I'm looking for simple and elegant. Black label with silver leaf border and lettering. Label needs to have the following information on it: Fern Hollow Candle Co. as the company name, scent name in the middle and in smaller font, it needs to say Made in USA, All Natural, 8oz. Attached photos are for inspiration.

Target Market(s)

People looking for high end, all natural candle fragrances

Industry/Entity Type

Candle-Spa

Colors

Designer to choose only greyscale colors for use in the design.

Requirements
Must have
• Company Name, Scent (ability to change scent names), All Natural, Made in USA, 8oz
Nice to have
• Black background, silver leaf border and silver leaf font. Elegant fonts maybe slightly cursive

```html
<!DOCTYPE html>
<html lang="en">
<head>
<meta charset="UTF-8">
<title>Fern Hollow Candle Co. – Cedarwood Label</title>
<link rel="stylesheet" href="https://fonts.googleapis.com/css2?family=Sacramento&family=Cormorant+Garamond:wght@400&family=Montserrat:wght@300;400&display=swap">
<style>
  :root {
    --page-bg: #d4d4d4;
    --label-black: #0d0d0d;
    --silver: #d2d2d2;
    --silver-soft: #bdbdbd;
  }
  * { margin: 0; padding: 0; box-sizing: border-box; }
  html, body {
    width: 1182px;
    height: 1200px;
    overflow: hidden;
    background: var(--page-bg);
  }
  .label {
    position: absolute;
    left: 41px;
    top: 164px;
    width: 1100px;
    height: 871px;
    background: var(--label-black);
    overflow: hidden;
  }
  .label__frame {
    position: absolute;
    left: 36px;
    right: 42px;
    top: 42px;
    bottom: 28px;
    border: 4px solid var(--silver);
  }
  .label__brand {
    position: absolute;
    left: 36px;
    right: 42px;
    top: 130px;
    text-align: center;
    font-family: "Sacramento", cursive;
    font-size: 178px;
    line-height: 1;
    white-space: nowrap;
    color: var(--silver);
  }
  .label__company-type {
    position: absolute;
    left: 36px;
    right: 42px;
    top: 418px;
    text-align: center;
    font-family: "Cormorant Garamond", serif;
    font-size: 58px;
    letter-spacing: 8px;
    color: var(--silver);
  }
  .label__scent {
    position: absolute;
    left: 36px;
    right: 42px;
    top: 612px;
    text-align: center;
    font-family: "Montserrat", sans-serif;
    font-weight: 300;
    font-size: 48px;
    letter-spacing: 13px;
    color: var(--silver-soft);
  }
  .label__details {
    position: absolute;
    left: 80px;
    right: 100px;
    top: 784px;
    display: flex;
    justify-content: space-between;
    font-family: "Montserrat", sans-serif;
    font-weight: 400;
    font-size: 36px;
    letter-spacing: 1.5px;
    color: var(--silver);
  }
</style>
</head>
<body>
  <div class="label">
    <div class="label__frame"></div>
    <div class="label__brand">Fern Hollow</div>
    <div class="label__company-type">CANDLE CO.</div>
    <div class="label__scent">CEDARWOOD</div>
    <div class="label__details">
      <span class="label__origin">MADE IN USA, ALL NATURAL</span>
      <span class="label__weight">8oz</span>
    </div>
  </div>
</body>
</html>
```